Web Design for an Online Dating Web Site

We need an uncoded web design for a new online dating web site called zMatchy.net. Simplicity and boldness are the key factors in the successful design.
Please look at the requirements document attached for details.
Updates
Dear all,
Please AVOID USING A PICTURE OF A HAPPY COUPLE ON THE HOME PAGE of the site. We highly want to move away from this space as it makes our web site just like another dating web site.
We like something simple with web 2.0 look and feel. The examples in the Requirements Document are exactly the design we are after.
Regards
Tarn
Industry/Entity Type
Dating
Look and feel
Each slider illustrates characteristics of the customer's brand and the style your logo design should communicate.

```html
<!DOCTYPE html>
<html lang="en">
<head>
<meta charset="utf-8">
<title>zMatchy.net – Home</title>
<link rel="stylesheet" href="https://fonts.googleapis.com/css2?family=Quicksand:wght@500;600;700&family=Noto+Sans:wght@400;700&display=swap">
<style>
:root{
  --pink:#e8117f;
  --pink-soft:#f266a8;
  --blue:#7fd1e6;
  --blue-deep:#1a8fb0;
  --grey:#8f8f94;
  --grey-light:#b5b5b5;
  --line:#d6d6d6;
  --bg:#ffffff;
  --text:#8a8a8a;
}
*{box-sizing:border-box;margin:0;padding:0}
html,body{width:1200px;height:900px;overflow:hidden;background:var(--bg)}
body{position:relative;font-family:"Noto Sans",sans-serif;color:var(--text)}

/* header */
.site-header{position:absolute;left:0;top:0;width:1200px;height:233px;
  background:linear-gradient(#fff 0,#fff 40px,#f2f2f2 228px);
  border-bottom:5px solid var(--line)}
.band{position:absolute;top:68px;height:40px;
  background:linear-gradient(#f48cc0 0,#f06aa9 45%,var(--pink) 55%,#f06aa9 100%)}
.band-left{left:0;width:148px;border-radius:0 20px 20px 0}
.band-right{left:600px;width:600px;border-radius:20px 0 0 20px}
.main-nav{position:absolute;left:625px;top:79px;display:flex;font-size:14.5px;color:#fff}
.main-nav a{color:#fff;text-decoration:none}
.main-nav .sep{margin:0 17px;opacity:.6}
.brand{position:absolute;left:170px;top:44px;display:flex;align-items:center;gap:14px}
.brand-dot{width:34px;height:34px;border-radius:50%;background:var(--pink)}
.brand-name{font-family:"Quicksand",sans-serif;font-weight:700;font-size:74px;color:var(--pink);line-height:1}
.login{position:absolute;left:625px;top:132px;display:flex;align-items:center;font-size:15px}
.login-label{color:var(--pink);width:58px}
.field{width:133px;height:28px;border:1px solid var(--grey-light);border-radius:14px;
  padding-left:12px;line-height:26px;color:var(--grey-light);margin-right:12px;background:#fff}
.go-btn{width:28px;height:28px;border-radius:50%;background:var(--pink);color:#fff;
  font-weight:700;font-size:13px;display:flex;align-items:center;justify-content:center}
.or{position:absolute;left:625px;top:162px;font-size:15px;color:var(--grey-light)}
.social{position:absolute;left:625px;top:180px;display:flex;align-items:center;font-size:15px;color:var(--grey-light)}
.social .sq{width:30px;height:30px;border-radius:3px;background:var(--pink);margin-right:8px}
.social .label{margin-right:8px}

/* hero */
.hero{position:absolute;left:0;top:233px;width:1200px;height:324px;
  background:linear-gradient(#f4f4f4,#fff 40%,#fafafa);border-bottom:5px solid var(--line)}
.hero-panel{position:absolute;left:150px;top:6px;width:899px;height:312px;
  border-left:1px solid #ececec;border-right:1px solid #ececec}
.hero-art{position:absolute;left:180px;top:72px;width:295px;height:120px;border-radius:10px;
  background:linear-gradient(90deg,#d6f0f7,#f1f1f3 50%,#fbdbe9)}
.hero-brand{position:absolute;left:495px;top:62px;font-family:"Quicksand",sans-serif;font-weight:700;
  font-size:104px;color:var(--pink);line-height:1}
.hero-wink{position:absolute;left:940px;top:62px;font-family:"Quicksand",sans-serif;font-weight:700;
  font-size:100px;color:var(--grey);line-height:1}
.hero-tagline{position:absolute;left:505px;top:208px;font-family:"Quicksand",sans-serif;font-weight:700;
  font-size:62px;color:var(--blue);letter-spacing:1px;line-height:1}
.arrow{position:absolute;top:125px}
.dots{position:absolute;top:574px;left:548px;display:flex;gap:8px}
.dots span{width:15px;height:15px;border-radius:50%;background:#d8d8d8;border:2px solid #e8e8e8}
.dots span.on{background:var(--blue)}

/* content */
.h2{position:absolute;font-family:"Quicksand",sans-serif;font-weight:700;font-size:23px;color:var(--grey)}
.signup-btn{position:absolute;left:145px;top:639px;width:439px;height:96px;border-radius:14px;
  border:1px solid #5aa9c0;
  background:linear-gradient(#b9ebf6 0,#7fd3e8 40%,#1b8fb0 55%,#1a85a5 85%,#5fc0da 100%);
  display:flex;align-items:center;padding-left:148px;
  font-family:"Quicksand",sans-serif;font-weight:700;font-size:54px;color:#fff}
.recover{position:absolute;left:145px;top:742px;font-size:15px;color:var(--text)}
.why-art{position:absolute;left:145px;top:827px;width:438px;height:80px;border:1px solid #dcdcdc;
  background:linear-gradient(#f7f7f7,#eee)}
.divider{position:absolute;left:598px;top:610px;width:1px;height:290px;background:var(--line)}
.post{position:absolute;left:611px;width:439px;height:96px;border:1px solid #c8c8c8;border-radius:14px;background:#fff}
.post-thumb{position:absolute;left:15px;top:10px;width:58px;height:56px;border:1px solid #d4d4d4;border-radius:4px;background:#f0f0f0}
.post-thumb.pink{background:linear-gradient(#fde3ef,#f7b9d6)}
.post-thumb.blue{background:linear-gradient(#e2f5fa,#b7e5f1)}
.post-text{position:absolute;left:88px;top:5px;width:345px;font-size:13.4px;line-height:16.5px;font-weight:700;color:var(--blue)}
.post-meta{display:block;font-weight:400;color:var(--text);margin-top:2px}
</style>
</head>
<body>

<header class="site-header">
  <div class="band band-left"></div>
  <div class="band band-right"></div>
  <nav class="main-nav">
    <a href="#">Why</a><span class="sep">|</span>
    <a href="#">How It Works</a><span class="sep">|</span>
    <a href="#">Sign Up</a><span class="sep">|</span>
    <a href="#">Our Blog</a>
  </nav>
  <div class="brand"><span class="brand-name">zMatchy</span><span class="brand-dot"></span></div>
  <div class="login">
    <span class="login-label">Longin</span>
    <span class="field">Username</span>
    <span class="field">Password</span>
    <span class="go-btn">go</span>
  </div>
  <div class="or">or</div>
  <div class="social">
    <span class="label">Login with your account in:</span>
    <span class="sq"></span><span class="sq"></span><span class="sq"></span><span class="sq"></span><span class="sq"></span>
    <span>more...</span>
  </div>
</header>

<section class="hero">
  <div class="hero-panel"></div>
  <svg class="arrow" style="left:50px" width="45" height="62" viewBox="0 0 45 62"><path d="M36 8 L12 31 L36 54" fill="none" stroke="var(--blue)" stroke-width="15" stroke-linecap="round" stroke-linejoin="round"/></svg>
  <svg class="arrow" style="left:1105px" width="45" height="62" viewBox="0 0 45 62"><path d="M9 8 L33 31 L9 54" fill="none" stroke="var(--pink-soft)" stroke-width="15" stroke-linecap="round" stroke-linejoin="round"/></svg>
  <div class="hero-art" role="img" aria-label="Illustration: two partners combining into a match"></div>
  <div class="hero-brand">zMatchy</div>
  <div class="hero-wink">;)</div>
  <div class="hero-tagline">why choose us?</div>
</section>
<div class="dots"><span class="on"></span><span></span><span></span><span></span><span></span></div>

<h2 class="h2" style="left:145px;top:607px">Join zmatchy.net</h2>
<a class="signup-btn">Sign Up ;)</a>
<p class="recover">Recover lost password</p>
<h2 class="h2" style="left:145px;top:789px">Why join zmatchy.net?</h2>
<div class="why-art" role="img" aria-label="Illustration explaining why to join"></div>

<div class="divider"></div>
<h2 class="h2" style="left:610px;top:607px">Recent Posts</h2>

<article class="post" style="top:639px">
  <div class="post-thumb pink"></div>
  <p class="post-text">Lorem ipsum dolor sit amet, consectetur adipiscing elit. Cras at felis sapien. Proin porttitor posuere bibendum. Nulla ac magna sit amet dolor elementum facilisis sit.
    <span class="post-meta">Sep 14, 2011 | 3 Comments | Read</span></p>
</article>
<article class="post" style="top:743px">
  <div class="post-thumb blue"></div>
  <p class="post-text">Lorem ipsum dolor sit amet, consectetur adipiscing elit. In pellentesque sapien eget nisi ornare rutrum. Cras laoreet blandit lectus, eget.
    <span class="post-meta">Sep 09, 2011 | 2 Comments | Read</span></p>
</article>
<article class="post" style="top:847px">
  <div class="post-thumb blue"></div>
  <p class="post-text">Nulla massa justo, pharetra et sollicitudin id, lacinia nec eros. Lorem ipsum dolor sit amet, consectetur adipiscing elit.</p>
</article>

</body>
</html>
```